Wooden Floor Website

I'd like a Modern and crisp site with emphasis on the site being easy to navigate through - services that we offer, gallery of previous work, history, who we are, contact, etc
https://vaultqx8261937-my.filedeckly.com/:b:/g/personal/tobias_pellwickhaus_co_uk/QWM7R2_kpLsTbNVafrxHoZWCKdYeP8u3G6vRPMsLmoXBtc

Coded - Design and coding required

5+ page

• Word Press Site

```html
<!DOCTYPE html>
<html lang="en">
<head>
<meta charset="utf-8">
<title>Pellwickhaus – Wood Flooring</title>
<link href="https://fonts.googleapis.com/css2?family=Poppins:wght@400;500;600;700&family=Open+Sans:wght@400;600&display=swap" rel="stylesheet">
<style>
:root{
  --brown:#b8702e;
  --brown-dark:#8a4f1c;
  --ink:#222;
  --text:#666;
  --muted:#999;
  --line:#e4e4e4;
  --band:#f3f3f3;
  --dark:#2b2b2b;
  --white:#fff;
}
*{margin:0;padding:0;box-sizing:border-box}
html,body{width:1200px;height:3656px;overflow:hidden}
body{position:relative;background:var(--white);font-family:"Open Sans",sans-serif;color:var(--text)}
.abs{position:absolute}
h2.section-title{font-family:"Poppins",sans-serif;font-weight:600;font-size:38px;color:var(--ink);text-align:center}

/* header */
.brand{left:176px;top:10px;display:flex;align-items:center;gap:10px}
.brand-mark{width:26px;height:26px;background:var(--ink)}
.brand-name{font-family:"Poppins",sans-serif;font-weight:600;font-size:13px;letter-spacing:1px;color:var(--ink)}
.top-links{left:585px;top:14px;display:flex;gap:28px;font-size:11px;font-family:"Poppins",sans-serif;color:var(--ink);letter-spacing:.5px}
.phone-box{left:828px;top:56px;width:150px;height:36px;border:1px solid var(--line);background:#f7f7f7;font-size:10px;padding:5px 10px;line-height:13px;color:var(--ink)}
.phone-box b{color:var(--brown)}
.main-nav{left:176px;top:70px;display:flex;gap:36px;font-family:"Poppins",sans-serif;font-size:11px;color:var(--ink)}
.search{left:1010px;top:62px}

/* hero */
.hero{left:118px;top:112px;width:964px;height:400px;background:linear-gradient(100deg,#e9e6e1 0%,#f4f2ee 45%,#d9d3ca 70%,#b9ab96 100%)}
.hero-kicker{left:176px;top:206px;font-family:"Poppins",sans-serif;font-size:22px;letter-spacing:3px;color:var(--ink)}
.hero-title{left:172px;top:232px;font-family:"Poppins",sans-serif;font-weight:700;font-size:60px;color:var(--ink);letter-spacing:1px}
.btn{left:176px;top:320px;width:122px;height:40px;background:var(--brown);color:#fff;font-family:"Poppins",sans-serif;font-size:11px;font-weight:600;display:flex;align-items:center;justify-content:center;letter-spacing:1px}
.cats{left:178px;top:448px;width:844px;height:110px;display:flex;background:#fff;box-shadow:0 6px 20px rgba(0,0,0,.1)}
.cat{flex:1;display:flex;flex-direction:column;align-items:center;justify-content:center;gap:10px;border-right:1px solid var(--line);font-family:"Poppins",sans-serif;font-size:10px;font-weight:600;color:var(--ink);text-align:center;line-height:13px}
.cat.active{background:var(--brown);color:#fff;margin-top:-14px;height:124px}
.arrow-btn{width:34px;height:34px;border-radius:50%;background:#fff;box-shadow:0 2px 8px rgba(0,0,0,.15);display:flex;align-items:center;justify-content:center;top:488px}

/* who we are */
.who-title{left:250px;top:656px;font-family:"Poppins",sans-serif;font-weight:600;font-size:36px;color:var(--ink)}
.who-rule{left:178px;top:676px;width:56px;height:3px;background:var(--ink)}
.who-lead{left:250px;top:716px;width:300px;font-size:16px;line-height:24px;color:var(--brown)}
.who-body{left:620px;top:666px;width:360px;font-size:12px;line-height:19px;color:var(--muted)}
.who-body p+p{margin-top:12px}

/* projects */
.band{left:0;top:1040px;width:1200px;height:740px;background:var(--band)}
.proj-title{left:0;top:1064px;width:1200px}
.proj-title-wrap{left:0;top:1060px;width:1200px}
.filters{left:178px;top:1158px;display:flex;gap:34px;font-size:11px;color:var(--muted);font-family:"Poppins",sans-serif}
.filters .on{color:var(--brown);border-bottom:2px solid var(--brown);padding-bottom:2px}
.grid{left:0;top:1210px;width:1200px;display:grid;grid-template-columns:repeat(4,1fr);grid-template-rows:230px 320px;gap:4px}
.photo{position:relative}
.photo span{position:absolute;right:10px;bottom:8px;font-size:9px;color:#fff;font-family:"Poppins",sans-serif;letter-spacing:.5px}
.wide{grid-column:3/5}

/* history */
.history{left:0;top:1780px;width:1200px;height:820px;background:linear-gradient(180deg,#fbfaf8,#eeebe6 50%,#f8f6f3)}
.timeline{left:598px;top:1990px;width:3px;height:470px;background:#a77a55}
.year{width:180px;height:44px;background:linear-gradient(90deg,#8a5a34,#b98a5e);color:#fff;font-family:"Poppins",sans-serif;font-weight:700;font-size:24px;display:flex;align-items:center;justify-content:center}
.year.left{clip-path:polygon(0 0,88% 0,100% 50%,88% 100%,0 100%)}
.year.right{clip-path:polygon(12% 0,100% 0,100% 100%,0 100%,0 50%, 12% 0)}
.entry{width:170px;font-size:9px;line-height:13px;color:var(--text)}
.entry b{display:block;font-family:"Poppins",sans-serif;font-size:12px;color:var(--ink);margin-bottom:4px}
.tick{width:20px;height:2px;background:#a77a55}

/* products */
.prod-row{left:178px;top:2834px;display:flex;gap:14px}
.prod{width:200px;text-align:center}
.prod .swatch{height:164px}
.prod p{margin-top:10px;font-family:"Poppins",sans-serif;font-weight:600;font-size:12px;color:var(--ink);line-height:16px}

/* footer */
.footer{left:118px;top:3190px;width:964px;height:410px;background:#f2f2f2}
.fcol{top:3262px;font-size:10px;line-height:20px;color:var(--text)}
.fcol h4{font-family:"Poppins",sans-serif;font-size:10px;font-weight:600;color:var(--ink);letter-spacing:1px;margin-bottom:8px}
.newsletter{left:858px;top:3160px;width:224px;height:360px;background:var(--dark);padding:30px 24px;color:#ccc;font-size:10px;line-height:16px}
.newsletter h3{font-family:"Poppins",sans-serif;font-weight:700;font-size:17px;line-height:21px;color:#fff;margin-bottom:14px}
.email{margin-top:18px;display:flex;height:32px}
.email div:first-child{flex:1;background:#fff;color:var(--muted);padding:8px 10px}
.email div:last-child{width:34px;background:var(--brown)}
.socials{margin-top:24px;display:flex;gap:10px}
.socials i{width:22px;height:22px;border-radius:50%;border:1px solid #777;display:block}
.socials i.on{background:var(--brown);border-color:var(--brown)}
.copy{left:178px;top:3540px;font-size:9px;color:var(--muted)}
</style>
</head>
<body>

<!-- header -->
<div class="abs brand"><div class="brand-mark"></div><div class="brand-name">PELLWICKHAUS</div></div>
<nav class="abs top-links"><span>OFFERS</span><span>SHOWROOMS</span><span>ABOUT US</span><span>BLOG</span><span>CONTACT</span></nav>
<nav class="abs main-nav"><span>SERVICES</span><span>WHO WE ARE</span><span>OUR WORK</span><span>HISTORY</span><span>FEATURED PRODUCTS</span><span>NEWS</span></nav>
<div class="abs phone-box">Call us today<br><b>+44 (0)20 7946 0321</b></div>
<svg class="abs search" width="14" height="14" viewBox="0 0 14 14"><circle cx="6" cy="6" r="4.5" fill="none" stroke="#222" stroke-width="1.5"/><line x1="9.5" y1="9.5" x2="13" y2="13" stroke="#222" stroke-width="1.5"/></svg>

<!-- hero -->
<div class="abs hero" role="img" aria-label="Bright room with light oak flooring, tall windows and a balcony"></div>
<div class="abs hero-kicker">THE BEST &amp; FINEST</div>
<div class="abs hero-title">FLOORING</div>
<div class="abs btn">GET A QUOTE</div>

<div class="abs arrow-btn" style="left:150px"><svg width="10" height="10" viewBox="0 0 10 10"><path d="M7 1 3 5l4 4" fill="none" stroke="#222" stroke-width="1.5"/></svg></div>
<div class="abs arrow-btn" style="left:1016px"><svg width="10" height="10" viewBox="0 0 10 10"><path d="M3 1l4 4-4 4" fill="none" stroke="#222" stroke-width="1.5"/></svg></div>
<div class="abs cats">
  <div class="cat"><svg width="34" height="28" viewBox="0 0 34 28"><path d="M3 14 17 3l14 11M7 11v15h20V11" fill="none" stroke="#b8702e" stroke-width="2"/></svg>CARPET<br>RESIDENTIAL</div>
  <div class="cat"><svg width="34" height="28" viewBox="0 0 34 28"><rect x="3" y="3" width="28" height="22" fill="none" stroke="#b8702e" stroke-width="2"/><path d="M3 10h28M3 17h28M14 3v7M22 10v7M10 17v8" stroke="#b8702e" stroke-width="2"/></svg>LUXURY VINYL<br>TILES (LVT)</div>
  <div class="cat active"><svg width="34" height="28" viewBox="0 0 34 28"><rect x="3" y="3" width="28" height="22" fill="none" stroke="#fff" stroke-width="2"/><path d="M3 10h28M3 17h28M18 3v7M10 10v7M24 17v8" stroke="#fff" stroke-width="2"/></svg>LAMINATE<br>FLOORING</div>
  <div class="cat"><svg width="34" height="28" viewBox="0 0 34 28"><path d="M3 18 17 8l14 10-14 8z" fill="none" stroke="#b8702e" stroke-width="2"/><path d="M3 12 17 2l14 10" fill="none" stroke="#b8702e" stroke-width="2"/></svg>ENGINEERED<br>WOOD</div>
  <div class="cat"><svg width="34" height="28" viewBox="0 0 34 28"><rect x="3" y="5" width="28" height="18" fill="none" stroke="#b8702e" stroke-width="2"/><path d="M3 14h28M17 5v18" stroke="#b8702e" stroke-width="2"/></svg>VINYL<br>FLOORING</div>
  <div class="cat" style="border-right:0"><svg width="34" height="28" viewBox="0 0 34 28"><path d="M3 25 13 3h8l10 22z" fill="none" stroke="#b8702e" stroke-width="2"/><path d="M8 15h18" stroke="#b8702e" stroke-width="2"/></svg>PARQUET<br>FLOORING</div>
</div>

<!-- who we are -->
<div class="abs who-rule"></div>
<h2 class="abs who-title">Who We Are</h2>
<p class="abs who-lead"><b>PELLWICKHAUS</b> offer a range of fully bespoke finished wood flooring in planks, herringbone blocks and chevrons; styles to suit any interior design.</p>
<div class="abs who-body">
  <p>With endless options available, you can choose the design, dimensions, grade, texture, colour and finish of products to order in the UK.</p>
  <p>Combining the finest sustainable oak with the latest state of the art machinery, finishing products and highly skilled craftsmen, we will together create your bespoke wood floor.</p>
</div>

<!-- projects -->
<div class="abs band"></div>
<div class="abs proj-title-wrap"><h2 class="section-title">Our Project</h2></div>
<div class="abs filters"><span class="on">All</span><span>Retail</span><span>Residential</span><span>Commercial</span><span>Food &amp; Drink</span><span>Manufacturing</span><span>Government</span><span>Highrise</span></div>
<div class="abs grid">
  <div class="photo" role="img" aria-label="Teal-walled lounge with oak floor" style="background:linear-gradient(180deg,#1f5a66,#2f6c73 55%,#a98a66)"><span>COMMERCIAL</span></div>
  <div class="photo" role="img" aria-label="Dining room with yellow chairs on oak floor" style="background:linear-gradient(180deg,#2f6f6f,#d1b04a 55%,#b89a74)"></div>
  <div class="photo" role="img" aria-label="Living room with orange sofa on light wood floor" style="background:linear-gradient(180deg,#e7e2da,#c9602f 50%,#c4a27c)"><span>RESIDENTIAL</span></div>
  <div class="photo" role="img" aria-label="Navy kitchen with dark wood floor" style="background:linear-gradient(180deg,#dcdcdc,#2c3a5a 50%,#8c6b4c)"><span>COMMERCIAL</span></div>
  <div class="photo" role="img" aria-label="Dark kitchen with grey oak floor" style="background:linear-gradient(180deg,#3a3a3a,#6a645c 55%,#7d7064)"><span>RESIDENTIAL</span></div>
  <div class="photo" role="img" aria-label="Dining area with chairs on parquet" style="background:linear-gradient(180deg,#cfc7bc,#8e6b55 50%,#a6836a)"><span>COMMERCIAL</span></div>
  <div class="photo wide" role="img" aria-label="Open kitchen with island and herringbone oak floor" style="background:linear-gradient(180deg,#bfc9c2,#e3ddd3 40%,#3b3b3e 60%,#b0885f)"><span>RESIDENTIAL</span></div>
</div>

<!-- history -->
<div class="abs history" role="img" aria-label="Light whitewashed wood plank background"></div>
<div class="abs" style="left:0;top:1880px;width:1200px"><h2 class="section-title">History</h2></div>
<div class="abs timeline"></div>

<div class="abs year left" style="left:300px;top:2004px">2014</div>
<div class="abs tick" style="left:580px;top:2025px"></div>
<div class="abs entry" style="left:620px;top:2004px"><b>Lorem ipsum dolor sit.</b>Sed ut perspiciatis unde omnis iste natus error sit voluptatem accusantium dolorem.</div>

<div class="abs year right" style="left:720px;top:2124px">2016</div>
<div class="abs tick" style="left:600px;top:2145px"></div>
<div class="abs entry" style="left:400px;top:2124px;text-align:right"><b>Lorem ipsum dolor sit.</b>Nemo enim ipsam voluptatem quia voluptas sit aspernatur aut odit fugit.</div>

<div class="abs year left" style="left:300px;top:2254px">2017</div>
<div class="abs tick" style="left:580px;top:2275px"></div>
<div class="abs entry" style="left:620px;top:2254px"><b>Lorem ipsum dolor sit.</b>Neque porro quisquam est qui dolorem ipsum quia dolor sit amet adipisci.</div>

<div class="abs year right" style="left:720px;top:2384px">2018</div>
<div class="abs tick" style="left:600px;top:2405px"></div>
<div class="abs entry" style="left:400px;top:2384px;text-align:right"><b>Lorem ipsum dolor sit.</b>Ut enim ad minima veniam quis nostrum exercitationem ullam corporis suscipit.</div>

<!-- products -->
<div class="abs" style="left:0;top:2730px;width:1200px"><h2 class="section-title">Features Products</h2></div>
<svg class="abs" style="left:86px;top:2906px" width="12" height="16" viewBox="0 0 12 16"><path d="M10 1 3 8l7 7" fill="none" stroke="#222" stroke-width="2.5"/></svg>
<svg class="abs" style="left:1102px;top:2906px" width="12" height="16" viewBox="0 0 12 16"><path d="M2 1l7 7-7 7" fill="none" stroke="#222" stroke-width="2.5"/></svg>
<div class="abs prod-row">
  <div class="prod"><div class="swatch" role="img" aria-label="Light oak herringbone sample" style="background:linear-gradient(135deg,#e6dccd,#cdbda4)"></div><p>Lorem ipsum dolor<br>sit amet.</p></div>
  <div class="prod"><div class="swatch" role="img" aria-label="Grey washed oak herringbone sample" style="background:linear-gradient(135deg,#a9a6a1,#7e7a74)"></div><p>Lorem ipsum dolor<br>sit amet.</p></div>
  <div class="prod"><div class="swatch" role="img" aria-label="Natural oak chevron sample" style="background:linear-gradient(135deg,#d9c2a0,#b8966a)"></div><p>Lorem ipsum dolor<br>sit amet.</p></div>
  <div class="prod"><div class="swatch" role="img" aria-label="Honey oak herringbone sample" style="background:linear-gradient(135deg,#d8b27c,#b98a52)"></div><p>Lorem ipsum dolor<br>sit amet.</p></div>
</div>

<!-- footer -->
<div class="abs footer"></div>
<div class="abs fcol" style="left:178px"><h4>NAVIGATION</h4>Offers<br>Showrooms<br>About Us<br>Blog<br>Contact</div>
<div class="abs fcol" style="left:290px"><h4>&nbsp;</h4>Services<br>Who we are<br>Our Work<br>History<br>Featured products</div>
<div class="abs fcol" style="left:420px"><h4>&nbsp;</h4>Terms and Conditions<br>Cookie Policy<br>Customer Reviews</div>
<div class="abs fcol" style="left:624px"><h4>QUICK LINKS</h4>Contact us<br>Fitting Guides<br>Delivery Options<br>Installation Returns<br>Sustainable Flooring</div>
<div class="abs newsletter">
  <h3>SUBSCRIBE TO<br>OUR NEWSLETTER</h3>
  <p>Lorem ipsum dolor sit amet consectetur adipiscing elit. Suspendisse varius enim in eros elementum tristique duis cursus mi quis viverra ornare eros dolor.</p>
  <div class="email"><div>Enter email</div><div></div></div>
  <div class="socials"><i></i><i></i><i class="on"></i><i></i><i></i></div>
</div>
<div class="abs copy">© 2018 PELLWICKHAUS. All Rights Reserved.</div>

</body>
</html>
```